Home Page for Prospix

We need to design a new home page for Prospix.com, a provider of B2B data for sales and marketing professionals.

The home page should follow the lead of our newly re-designed header and logo (still being tweaked) and use our new color scheme. Please refer to attached file. Please use this file as as the basis of the design for the rest or the home page. No part of the header or logo needs to be altered in this project.

All submissions should be clear, fresh, clean and simple in style. We like the look and feel of tallyvine.com, costharbor.com and pollquarry.com. Please use them as references.

The main functions of the home page will be to tell the user about 1) the benefits and uses of Prospix and 2) to get them to sign up.

Based upon the successful redesign of our homepage, we will also be redesigning our subscription page and our about us page in the coming weeks.

Target Market(s)

Sales and marketing professionals. Mostly 25 - 45 year old males.

Industry/Entity Type

Marketing

Requirements
Must have
• Items needed:

1A) There should be three main points highlighted 1) Fresh Data 2) Sales Intelligence 3) Increased Bottomline. There will be further text under these headers tbd. For style/feel reference the same device used by pollquarry uses on its homepage.

1B) When you rollover these three items they should highlight and be clickable. The click will lead you to a header and paragraph about each that is further down the homepage (text tbd).

2) We also need a free trial and a sign up button. This button should move with you as you scroll up and down the homepage. Reference www.tallyvine.com.

3) We need a “Featured In” section. Also reference tallyvine.com. You can pull the content from prospix.com’s current home page.

4) We also need a social media buttons section (chatterlane, quipstream, orbitly+ and workNest)

```html
<!DOCTYPE html>
<html lang="en">
<head>
<meta charset="utf-8">
<title>Prospix – Home</title>
<link rel="stylesheet" href="https://fonts.googleapis.com/css2?family=Ubuntu:wght@300;400;500;700&display=swap">
<style>
:root{
  --blue:#1ea3e2;
  --blue-light:#45c3f5;
  --blue-dark:#0e8fcf;
  --ink:#333333;
  --ink-soft:#666666;
  --line:#d9d9d9;
  --panel:#f1efef;
  --footer:#2b2b2b;
  --logo-grey:#9a9a9a;
  --white:#ffffff;
}
*{margin:0;padding:0;box-sizing:border-box}
html,body{width:1100px;height:1200px;overflow:hidden;background:var(--white)}
body{position:relative;font-family:"Ubuntu",sans-serif;color:var(--ink)}
a{color:inherit;text-decoration:none}

.brand{position:absolute;left:138px;top:42px;font-size:54px;font-weight:500;color:var(--blue);letter-spacing:-1px;font-family:"Ubuntu",sans-serif}

.main-nav{position:absolute;left:110px;top:128px;width:880px;height:44px;
  background:linear-gradient(var(--blue-light),var(--blue));border-top:1px solid #8fd9f8}
.main-nav ul{list-style:none;display:flex;margin-left:38px;height:100%}
.main-nav li{height:100%;display:flex;align-items:center;padding:0 28px;color:var(--white);font-size:13px;font-weight:500}
.main-nav li.active{background:#000;padding:0 26px}

.login-box{position:absolute;left:750px;top:48px;width:218px;height:185px;background:var(--white);
  border:1px solid #d6d6d6;box-shadow:0 1px 3px rgba(0,0,0,.12);z-index:3}
.login-tabs{height:42px;background:linear-gradient(var(--blue-light),var(--blue-dark));border-radius:3px 3px 0 0;
  display:flex;align-items:center;color:var(--white);font-size:12.5px;position:relative}
.login-tabs .tab{padding:0 14px;display:flex;align-items:center;gap:8px}
.login-tabs .tab+.tab{border-left:1px solid rgba(255,255,255,.5)}
.login-tabs .toggle{position:absolute;right:0;bottom:-1px;width:22px;height:20px;background:var(--white);border:1px solid #bbb;display:flex;align-items:center;justify-content:center}
.login-box .field{display:block;margin:20px 0 0 14px;width:190px;height:30px;border:1px solid #ddd;border-radius:4px;
  font-size:10.5px;color:#999;padding:9px 10px;box-shadow:inset 0 1px 2px rgba(0,0,0,.08)}
.login-box .field+.field{margin-top:12px}
.login-box .submit{display:block;margin:15px auto 0;width:88px;height:28px;border-radius:3px;background:linear-gradient(var(--blue-light),var(--blue));
  color:var(--white);font-size:14px;text-align:center;line-height:28px;font-weight:500}

.hero{position:absolute;left:110px;top:195px;width:880px;height:335px;border:1px solid var(--line)}
.hero-inner{position:absolute;left:19px;top:17px;width:842px;height:300px;background:var(--panel);border:1px solid #ddd}
.hero-photo{position:absolute;right:0;top:0;width:400px;height:100%;
  background:linear-gradient(90deg,var(--panel),#c9d2da 25%,#8c98a5 60%,#3a4350)}
.hero h1{position:absolute;left:42px;top:32px;font-size:33px;font-weight:400;line-height:40px;color:#444;letter-spacing:-.5px}
.hero h1 b{font-weight:700}
.hero p{position:absolute;left:42px;top:127px;width:345px;font-size:13px;line-height:21.5px;color:#222}
.hero .btn-read{position:absolute;left:42px;top:201px;width:130px;height:40px;border-radius:4px;
  background:linear-gradient(var(--blue-light),var(--blue));color:var(--white);font-size:18px;text-align:center;line-height:40px}
.hero .dots{position:absolute;left:49px;top:262px;display:flex;gap:7px}
.hero .dots span{width:10px;height:10px;border-radius:50%;background:#111}
.hero .dots span:first-child{background:var(--blue)}

.section-title{font-weight:300;font-size:29px;color:#222;letter-spacing:-.5px}
.welcome{position:absolute;left:122px;top:556px;width:510px}
.welcome-photo{position:absolute;left:0;top:48px;width:88px;height:86px;background:linear-gradient(#e9ecef,#c9ced4)}
.welcome p{position:absolute;left:122px;top:47px;width:390px;font-size:10.2px;line-height:15.6px;color:var(--ink-soft);font-weight:300}

.news{position:absolute;left:709px;top:556px;width:268px}
.news p{margin-top:18px;font-size:10.2px;line-height:16px;color:var(--ink-soft);font-weight:300}
.news .date{margin-top:8px;font-size:10.5px;color:var(--blue)}
.news .view-all{display:block;text-align:right;margin-top:8px;font-size:11px;color:var(--blue)}

.feature{position:absolute;top:738px;width:276px}
.feature h2{font-size:20px;font-weight:400;color:var(--blue);letter-spacing:.2px;margin-left:1px}
.feature .frame{margin-top:13px;height:111px;border:1px solid #e2e2e2;padding:5px;box-shadow:0 1px 2px rgba(0,0,0,.05)}
.feature .photo{height:100%}
.feature p{margin:20px 6px 0;font-size:13px;line-height:18.5px;color:#333}
.feature p u{text-decoration:underline}
.feature .more{display:flex;align-items:center;gap:4px;margin:8px 6px 0;font-size:10px;color:var(--blue)}

.featured-in{position:absolute;left:125px;top:1000px;width:853px;height:24px}
.featured-in .rule{position:absolute;top:15px;height:1px;background:#bbb}
.featured-in h3{position:absolute;left:0;right:0;text-align:center;font-size:18px;font-weight:400;color:#444}
.press{position:absolute;left:140px;top:1040px;width:830px;display:flex;justify-content:space-between;align-items:center;height:60px}
.press span{font-size:20px;font-weight:700;color:var(--logo-grey);letter-spacing:-.5px}

.site-footer{position:absolute;left:0;top:1132px;width:1100px;height:68px;background:var(--footer)}
.footer-links{position:absolute;left:138px;top:14px;display:flex;gap:26px;font-size:12px;color:#ddd}
.copyright{position:absolute;left:136px;top:42px;font-size:11px;color:#ccc}
.social{position:absolute;right:60px;top:22px;display:flex;gap:10px}
.social a{display:flex;align-items:center;gap:4px;font-size:10.5px;color:#eee}
.social a i{width:10px;height:10px;background:var(--blue);border-radius:2px;display:block}
</style>
</head>
<body>

<header>
  <div class="brand">Prospix</div>

  <div class="login-box">
    <div class="login-tabs">
      <span class="tab">
        <svg width="18" height="16" viewBox="0 0 18 16"><circle cx="9" cy="5" r="4" fill="#111"/><path d="M1 16c0-5 4-7 8-7s8 2 8 7z" fill="#111"/></svg>
        Sign Up
      </span>
      <span class="tab">User Login</span>
      <span class="toggle"><svg width="10" height="6" viewBox="0 0 10 6"><path d="M0 0h10L5 6z" fill="#111"/></svg></span>
    </div>
    <span class="field">Username</span>
    <span class="field">Password</span>
    <a class="submit" href="#">Submit</a>
  </div>

  <nav class="main-nav">
    <ul>
      <li class="active">New</li>
      <li>People</li>
      <li>Companies</li>
      <li>Downloads</li>
    </ul>
  </nav>
</header>

<section class="hero">
  <div class="hero-inner">
    <div class="hero-photo" role="img" aria-label="Photo of a smiling business team meeting around a table in a bright office"></div>
    <h1>Benifits and <b>Uses</b> of<br><b>Prospix</b></h1>
    <p>Lorem Ipsum is simply dummy text of the printing and typesetting industry. Lorem Ipsum has been the industry's standard dummy text ever since the 1500s, when an......</p>
    <a class="btn-read" href="#">Read More</a>
    <div class="dots"><span></span><span></span><span></span></div>
  </div>
</section>

<section class="welcome">
  <h2 class="section-title">Welcome to our site</h2>
  <div class="welcome-photo" role="img" aria-label="Photo of a scientist in a white coat at a microscope"></div>
  <p>Lorem Ipsum is simply dummy text of the printing and typesetting industry. Lorem Ipsum has been the industry's standard dummy text ever since the 1500s, when an unknown printer took a galley of type and scrambled it to make a type specimen book. It has survived not only five centuries, but also the leap into emore recently with desktop publishing software like Quillset Composer including versions of Lorem Ipsum.</p>
</section>

<section class="news">
  <h2 class="section-title">News Release</h2>
  <p>Lorem Ipsum is simply dummy text of the printing and typesetting industry. Lorem Ipsum has been the industry's standard dummy text ever since the 1500s, when an</p>
  <div class="date">06/03/2012</div>
  <a class="view-all" href="#">View All</a>
</section>

<article class="feature" style="left:119px">
  <h2>FRESH DATA</h2>
  <div class="frame"><div class="photo" role="img" aria-label="Photo of a man lying on the floor working on a laptop" style="background:linear-gradient(90deg,#e9ecee,#cfd3d6 55%,#6f6a66)"></div></div>
  <p>Maecenas ullamcorper nibh vitae erat. Nunc hendrerit viverra urna. Ffelis arcu luctus eros, ac semper quam turpis ut tellus.</p>
  <a class="more" href="#">MORE <svg width="16" height="6" viewBox="0 0 16 6"><path d="M0 3h15M12 .5 15 3l-3 2.5" stroke="#1ea3e2" fill="none"/></svg></a>
</article>

<article class="feature" style="left:412px">
  <h2>SALES INTELLIGENCE</h2>
  <div class="frame"><div class="photo" role="img" aria-label="Photo of a call centre agent wearing a headset" style="background:linear-gradient(90deg,#5a6068,#3f444b 60%,#6a5a52)"></div></div>
  <p>Ffelis arcu luctus eros, ac semper quam turpis ut tellus. Etiam sed ipsum. <u>Quisque et urna.</u> Praesent vehicula, libero non aliquet pretium,</p>
  <a class="more" href="#">MORE <svg width="16" height="6" viewBox="0 0 16 6"><path d="M0 3h15M12 .5 15 3l-3 2.5" stroke="#1ea3e2" fill="none"/></svg></a>
</article>

<article class="feature" style="left:706px">
  <h2>INCREASED BOTTOMLINE</h2>
  <div class="frame"><div class="photo" role="img" aria-label="Illustration of two businessmen beside a rising bar chart with an upward arrow" style="background:linear-gradient(#ffffff,#eef1f4)"></div></div>
  <p>Maecenas ullamcorper nibh vitae erat. Nunc hendrerit viverra urna. <u>Etiam sed ipsum.</u> Quisque et urna.</p>
  <a class="more" href="#">MORE <svg width="16" height="6" viewBox="0 0 16 6"><path d="M0 3h15M12 .5 15 3l-3 2.5" stroke="#1ea3e2" fill="none"/></svg></a>
</article>

<section>
  <div class="featured-in">
    <span class="rule" style="left:0;width:362px"></span>
    <h3>Featured In:</h3>
    <span class="rule" style="right:0;width:356px"></span>
  </div>
  <div class="press">
    <span>Trendwire</span><span>Newsgrid</span><span>stackform</span><span>techpost</span>
    <span>Trendwire</span><span>Newsgrid</span><span>stackform</span><span>techpost</span>
  </div>
</section>

<footer class="site-footer">
  <nav class="footer-links">
    <a href="#">About Us</a><a href="#">Contact Us</a><a href="#">Team</a><a href="#">Customers</a><a href="#">Jobs</a><a href="#">Sign Up</a>
  </nav>
  <div class="copyright">© 2013 Prospix Corporation. All Rights Reserved</div>
  <div class="social">
    <a href="#"><i></i>chatterlane</a>
    <a href="#"><i></i>quipstream</a>
    <a href="#"><i></i>orbitly+</a>
    <a href="#"><i></i>workNest</a>
  </div>
</footer>

</body>
</html>
```